Anzeigengestaltung für Steuerberaterin
Zielgruppe
Ich bin Steuerberaterin und Zertizierter Testamentsvollstrecker (BKW) in Lindenau.
Wir sind keine kleine, innovative Steuerkanzlei und möchten vor allem Mandanten ansprechen, den eine digitale Zusammenarbeit wichtig ist.
Zielgruppe: Startups, kleine Unternehmen oder Freiberufler, Gemeinnützige Organisationen
Software: Datev, Buchhaltungsbutler, sevDesk
Aufgabenstellung
Nach meinem Umzug in größere Büroräume benötige ich eine Anzeige im Format 90 x 80 mm für eine Zeitung.
Auf der Anzeige sollte ein Umzugshinweis enthalten sein. Die Anzeige würde ich gerne wieder verwenden. (eine version ohne Umzugshinweis)
Slogan: Miteinander Zukunft Planen

```html
<!DOCTYPE html>
<html lang="de">
<head>
<meta charset="utf-8">
<title>Anzeige Steuerkanzlei Lotte Krause – mit und ohne Umzugshinweis</title>
<link href="https://fonts.googleapis.com/css2?family=Jost:wght@300;400;500&display=swap" rel="stylesheet">
<style>
  :root {
    --stage: #d9d9d9;
    --paper: #ffffff;
    --brand-blue: #1a4fa0;
    --accent-cyan: #14b4e8;
    --slogan-gray: #8a8d90;
    --band-gray: #a7a9ac;
    --frame: #6f6f6f;
    --logo-ink: #3a3d42;
  }
  * { box-sizing: border-box; margin: 0; padding: 0; }
  html, body { width: 1200px; height: 676px; overflow: hidden; }
  body {
    background: var(--stage);
    font-family: "Jost", "Futura", sans-serif;
    position: relative;
  }
  .ad {
    position: absolute;
    top: 117px;
    width: 545px;
    height: 485px;
    background: var(--paper);
    border: 1px solid var(--frame);
    overflow: hidden;
  }
  .ad--moving { left: 26px; }
  .ad--standard { left: 636px; }

  .ad__photo {
    position: absolute;
    inset: 0 0 auto 0;
    height: 360px;
    background:
      linear-gradient(to bottom, rgba(255,255,255,0) 55%, #fff 100%),
      radial-gradient(ellipse 30% 45% at 40% 60%, rgba(226,110,130,0.75), rgba(226,110,130,0) 70%),
      radial-gradient(ellipse 22% 30% at 35% 22%, rgba(170,110,70,0.7), rgba(170,110,70,0) 70%),
      radial-gradient(ellipse 25% 55% at 72% 45%, rgba(40,70,90,0.55), rgba(40,70,90,0) 70%),
      radial-gradient(ellipse 20% 50% at 8% 45%, rgba(150,120,100,0.6), rgba(150,120,100,0) 70%),
      linear-gradient(100deg, #e9dcd6 0%, #f1e6e2 45%, #d9eef0 80%, #cfe9ee 100%);
  }

  .ad__headline {
    position: absolute;
    left: 17px;
    top: 255px;
    color: var(--brand-blue);
    font-weight: 400;
    font-size: 37px;
    line-height: 35px;
    letter-spacing: -0.3px;
    white-space: nowrap;
  }
  .ad__subline {
    position: absolute;
    left: 17px;
    top: 333px;
    color: var(--brand-blue);
    font-size: 21px;
    line-height: 25px;
    letter-spacing: 0.2px;
    white-space: nowrap;
  }
  .ad__bands {
    position: absolute;
    left: 0; top: 370px;
    width: 545px; height: 70px;
  }
  .ad__info {
    position: absolute;
    left: 17px;
    top: 431px;
    color: var(--brand-blue);
    font-size: 19px;
    white-space: nowrap;
  }
  .ad__slogan {
    position: absolute;
    left: 17px;
    top: 455px;
    color: var(--slogan-gray);
    font-weight: 300;
    font-size: 21px;
    white-space: nowrap;
  }
  .ad__brand {
    position: absolute;
    right: 8px;
    bottom: 8px;
    width: 114px;
    text-align: center;
    color: var(--logo-ink);
    font-weight: 500;
  }
  .ad__brand-mark {
    display: block;
    width: 26px; height: 26px;
    margin: 0 auto 8px;
    background: var(--brand-blue);
  }
  .ad__brand-line1 { display: block; font-size: 7.5px; letter-spacing: 3.7px; line-height: 9px; }
  .ad__brand-line2 { display: block; font-size: 13px; letter-spacing: 1px; line-height: 14px; }

  .ad__badge {
    position: absolute;
    right: 0; top: 0;
    width: 216px; height: 66px;
  }
  .ad__badge text {
    font-family: "Jost", "Futura", sans-serif;
    font-size: 21px;
    fill: #ffffff;
  }
</style>
</head>
<body>

  <article class="ad ad--moving">
    <div class="ad__photo" role="img" aria-label="Foto: Team im Büro arbeitet an einem Bildschirm, überlagert von einem feinen Netzwerkmuster"></div>
    <svg class="ad__badge" viewBox="0 0 216 66" aria-label="Wir sind umgezogen!">
      <polygon points="0,33 216,0 216,33 3,64" fill="var(--accent-cyan)"/>
      <text x="10" y="54" transform="rotate(-9 10 54)">Wir sind umgezogen!</text>
    </svg>
    <h1 class="ad__headline">Ihre Steuerkanzlei für morgen<br>direkt im Zentrum von Lindenau</h1>
    <p class="ad__subline">Startups, kleine Unternehmen und Freiberufler<br>liegen uns ganz besonders am Herzen!</p>
    <svg class="ad__bands" viewBox="0 0 545 70" preserveAspectRatio="none" aria-hidden="true">
      <polygon points="30,57 545,8 545,20 30,62" fill="var(--band-gray)"/>
      <polygon points="0,42 545,4 545,7 0,57" fill="var(--brand-blue)"/>
    </svg>
    <p class="ad__info">Mehr Infos unter www.steuerkanzlei-krause.de</p>
    <p class="ad__slogan">Miteinander Zukunft Planen</p>
    <div class="ad__brand">
      <span class="ad__brand-mark"></span>
      <span class="ad__brand-line1">STEUERKANZLEI</span>
      <span class="ad__brand-line2">LOTTE KRAUSE</span>
    </div>
  </article>

  <article class="ad ad--standard">
    <div class="ad__photo" role="img" aria-label="Foto: Team im Büro arbeitet an einem Bildschirm, überlagert von einem feinen Netzwerkmuster"></div>
    <h1 class="ad__headline">Ihre Steuerkanzlei für morgen<br>direkt im Zentrum von Lindenau</h1>
    <p class="ad__subline">Startups, kleine Unternehmen und Freiberufler<br>liegen uns ganz besonders am Herzen!</p>
    <svg class="ad__bands" viewBox="0 0 545 70" preserveAspectRatio="none" aria-hidden="true">
      <polygon points="30,57 545,8 545,20 30,62" fill="var(--band-gray)"/>
      <polygon points="0,42 545,4 545,7 0,57" fill="var(--brand-blue)"/>
    </svg>
    <p class="ad__info">Mehr Infos unter www.steuerkanzlei-krause.de</p>
    <p class="ad__slogan">Miteinander Zukunft Planen</p>
    <div class="ad__brand">
      <span class="ad__brand-mark"></span>
      <span class="ad__brand-line1">STEUERKANZLEI</span>
      <span class="ad__brand-line2">LOTTE KRAUSE</span>
    </div>
  </article>

</body>
</html>
```